Social Media Infographic for White Paper

Am working on a white paper on social media use by C-Suite Executives, and hope to include some infographics. I would like some help designing the first infographic.

The master bit of information is that "66% of C-Suite Executives use social media for professional purpose."

Within that 66%
-70% post original content on a daily/weekly basis
-13% of professional users are lurkers
-40% plan to use social media even more in the future

After initial design will need to two versions of the infographic, one listing the source at the bottom in small print (Source: 2017 Venmoor Partners Executive Social Media Study), the other one with no source information.

Infographic design should be complimentary with my website: www.venmoorpartners.example, but use of green should be very limited, if at all.

Target Market(s)

New media, C-Suite Executives, Executive Coaches

Industry/Entity Type

Management Consulting

Font styles to use
Sans Serif

Requirements
Must have
• Infographic with data displayed in a easy to understand format that tells the story of C-Suite Executives that participate in social media for professional purposes.
Nice to have
• Complements website design - www.venmoor.example.
Should not have
• Limit use of green from website logo, which can be overpowering. Some is ok, but not too much

```html
<!DOCTYPE html>
<html lang="en">
<head>
<meta charset="utf-8">
<title>C-Suite Executives – Social Media Infographic</title>
<link rel="stylesheet" href="https://fonts.googleapis.com/css2?family=Oswald:wght@500&family=Saira+Semi+Condensed:wght@500&family=Roboto:ital,wght@0,400;0,700;1,300&display=swap">
<style>
  :root {
    --bg: #e1efe3;
    --halo: #b9e1d5;
    --navy: #14303f;
    --media-blue: #1a7fbd;
    --orange: #c8602a;
    --teal: #1f8fae;
    --ink: #1c2526;
    --phone: #4a4a4a;
    --phone-edge: #3b3b3b;
    --screen: #ffffff;
    --screen-shade: #e7e8ea;
    --ring-1: #1d3c4f;
    --ring-2: #2a6b8c;
    --ring-3: #1e8db6;
    --ring-4: #2f5e73;
    --stat: #444444;
    --data-a: #2f8aa8;
    --data-a-dark: #23697f;
    --data-b: #4dbb9e;
    --data-b-dark: #3a9179;
    --data-c: #f08a36;
    --data-c-dark: #c46c24;
    --person-on: #7cb342;
    --person-off: #9a9a9a;
    --bubble: #1a9ad6;
    --figure: #1c2e3a;
  }
  * { margin: 0; padding: 0; box-sizing: border-box; }
  html, body { width: 1200px; height: 720px; overflow: hidden; background: var(--bg); }
  .infographic { display: block; width: 1200px; height: 720px; }
  .title-social { font-family: "Oswald", sans-serif; font-size: 80px; fill: var(--navy); }
  .title-media { font-family: "Oswald", sans-serif; font-size: 80px; fill: var(--media-blue); }
  .title-infographic { font-family: "Oswald", sans-serif; font-size: 40px; fill: var(--orange); }
  .heading-csuite { font-family: "Saira Semi Condensed", sans-serif; font-size: 46px; fill: var(--teal); }
  .heading-exec { font-family: "Saira Semi Condensed", sans-serif; font-size: 50px; fill: var(--ink); }
  .stat-main { font-family: "Roboto", sans-serif; font-weight: 700; font-size: 38px; fill: var(--stat); }
  .stat-caption, .data-caption { font-family: "Roboto", sans-serif; font-style: italic; font-weight: 300; fill: var(--ink); }
  .stat-caption { font-size: 14px; }
  .data-caption { font-size: 19px; }
  .data-label { font-family: "Roboto", sans-serif; font-size: 16px; fill: #ffffff; letter-spacing: 0.5px; }
  .data-figure { font-family: "Oswald", sans-serif; font-size: 32px; fill: var(--figure); }
  .person-on { fill: var(--person-on); }
  .person-off { fill: var(--person-off); }
</style>
</head>
<body>
<svg class="infographic" viewBox="0 0 1200 720" xmlns="http://www.w3.org/2000/svg">
  <defs>
    <symbol id="person" viewBox="0 0 12 34">
      <circle cx="6" cy="4" r="4"/>
      <rect x="0.5" y="9" width="11" height="13" rx="2"/>
      <rect x="1.5" y="20" width="3.6" height="14"/>
      <rect x="6.9" y="20" width="3.6" height="14"/>
    </symbol>
    <linearGradient id="network-tones" x1="0" y1="0" x2="1" y2="1">
      <stop offset="0" stop-color="#cfe6c6"/>
      <stop offset="0.5" stop-color="#c4e3dc"/>
      <stop offset="1" stop-color="#f3e2b5"/>
    </linearGradient>
  </defs>

  <!-- Social media title block -->
  <g class="title-block">
    <circle cx="238" cy="408" r="180" fill="var(--halo)"/>
    <rect x="52" y="124" width="364" height="268" rx="40" fill="url(#network-tones)" opacity="0.85"
          role="img" aria-label="Network of connected social media user avatars"/>
    <g class="chat-bubble">
      <rect x="218" y="326" width="66" height="48" rx="6" fill="var(--bubble)"/>
      <polygon points="262,372 282,392 278,372" fill="var(--bubble)"/>
      <circle cx="237" cy="352" r="5" fill="#fff"/>
      <circle cx="251" cy="352" r="5" fill="#fff"/>
      <circle cx="265" cy="352" r="5" fill="#fff"/>
    </g>
    <text class="title-social" x="242" y="452" text-anchor="middle">SOCIAL</text>
    <text class="title-media" x="242" y="524" text-anchor="middle">MEDIA</text>
    <text class="title-infographic" x="240" y="564" text-anchor="middle">INFOGRAPHIC</text>
  </g>

  <!-- Heading -->
  <g class="heading">
    <text class="heading-csuite" x="463" y="128">C-Suite</text>
    <text class="heading-exec" x="463" y="175">Executives</text>
    <g class="magnifier" fill="none" stroke="#1a5f85" stroke-linecap="round">
      <circle cx="672" cy="100" r="28" stroke-width="7"/>
      <line x1="693" y1="121" x2="722" y2="152" stroke-width="8"/>
    </g>
  </g>

  <!-- Phone with main statistic -->
  <g class="phone">
    <rect x="462" y="188" width="274" height="464" rx="34" fill="var(--phone-edge)"/>
    <rect x="452" y="186" width="272" height="464" rx="34" fill="var(--phone)"/>
    <rect x="524" y="204" width="124" height="14" rx="7" fill="#fff"/>
    <rect x="474" y="234" width="226" height="358" rx="4" fill="var(--screen)"/>
    <polygon points="474,234 700,592 474,592" fill="var(--screen)"/>
    <polygon points="560,234 700,234 700,592" fill="var(--screen-shade)" opacity="0"/>
    <polygon points="474,234 560,234 700,460 700,592" fill="var(--screen-shade)" opacity="0.0"/>
    <polygon points="520,234 700,234 700,540" fill="#ffffff"/>
    <polygon points="474,234 520,234 700,540 700,592 474,592" fill="var(--screen-shade)" opacity="0"/>
    <polygon points="540,592 700,592 700,300 520,234" fill="var(--screen-shade)"/>
    <polygon points="474,234 540,234 700,500 700,592 474,592" fill="var(--screen)" opacity="0"/>
    <circle cx="586" cy="621" r="18" fill="#fff"/>
    <circle cx="554" cy="621" r="7" fill="#fff"/>
    <circle cx="618" cy="621" r="7" fill="#fff"/>

    <g class="donut" fill="none">
      <path d="M598 304 A104 104 0 0 1 670 333" stroke="var(--ring-1)" stroke-width="14"/>
      <path d="M598 304 A104 104 0 0 0 526 333" stroke="var(--ring-1)" stroke-width="14"/>
      <path d="M526 333 A104 104 0 0 0 500 410" stroke="var(--ring-4)" stroke-width="14"/>
      <path d="M500 410 A104 104 0 0 0 526 483" stroke="var(--ring-2)" stroke-width="14"/>
      <path d="M526 483 A104 104 0 0 0 598 512" stroke="var(--ring-2)" stroke-width="14"/>
      <path d="M598 512 A104 104 0 0 0 670 483" stroke="var(--ring-3)" stroke-width="14"/>
      <path d="M560 330 A86 86 0 0 1 640 332" stroke="var(--ring-3)" stroke-width="20"/>
      <path d="M560 330 A86 86 0 0 0 512 410" stroke="var(--ring-2)" stroke-width="20"/>
      <path d="M512 410 A86 86 0 0 0 556 485" stroke="#2b7fa5" stroke-width="20"/>
      <path d="M556 485 A86 86 0 0 0 640 470" stroke="var(--ring-4)" stroke-width="20"/>
    </g>
    <text class="stat-main" x="600" y="423" text-anchor="middle">66%</text>
    <text class="stat-caption" x="483" y="554">executives use sosial media for</text>
    <text class="stat-caption" x="483" y="573">professional purposes</text>
  </g>

  <!-- Data A -->
  <g class="data-row data-a">
    <use href="#person" x="756" y="224" width="12" height="34" class="person-on"/>
    <use href="#person" x="770" y="224" width="12" height="34" class="person-on"/>
    <use href="#person" x="784" y="224" width="12" height="34" class="person-on"/>
    <use href="#person" x="798" y="224" width="12" height="34" class="person-on"/>
    <polygon points="816,250 1044,250 1044,240 1084,262 1044,284 1044,266 838,266 838,264 816,250" fill="var(--data-a)"/>
    <polygon points="816,250 838,264 816,264" fill="var(--data-a-dark)"/>
    <rect x="750" y="264" width="88" height="24" fill="var(--data-a)"/>
    <text class="data-label" x="764" y="282">DATA A</text>
    <text class="data-figure" x="1092" y="279">70%</text>
    <text class="data-caption" x="846" y="304">post original content</text>
    <text class="data-caption" x="846" y="328">on a daily/weekly basis</text>
  </g>

  <!-- Data B -->
  <g class="data-row data-b">
    <use href="#person" x="756" y="352" width="12" height="34" class="person-on"/>
    <use href="#person" x="770" y="352" width="12" height="34" class="person-on"/>
    <use href="#person" x="784" y="352" width="12" height="34" class="person-off"/>
    <use href="#person" x="798" y="352" width="12" height="34" class="person-off"/>
    <polygon points="816,378 928,378 928,368 968,390 928,412 928,394 838,394 838,392 816,378" fill="var(--data-b)"/>
    <polygon points="816,378 838,392 816,392" fill="var(--data-b-dark)"/>
    <rect x="750" y="392" width="88" height="24" fill="var(--data-b)"/>
    <text class="data-label" x="764" y="410">DATA B</text>
    <text class="data-figure" x="980" y="406">13%</text>
    <text class="data-caption" x="846" y="432">of professional</text>
    <text class="data-caption" x="846" y="456">users are lurkers</text>
  </g>

  <!-- Data C -->
  <g class="data-row data-c">
    <use href="#person" x="756" y="482" width="12" height="34" class="person-on"/>
    <use href="#person" x="770" y="482" width="12" height="34" class="person-on"/>
    <use href="#person" x="784" y="482" width="12" height="34" class="person-on"/>
    <use href="#person" x="798" y="482" width="12" height="34" class="person-off"/>
    <polygon points="816,506 987,506 987,496 1026,518 987,540 987,522 838,522 838,520 816,506" fill="var(--data-c)"/>
    <polygon points="816,506 838,520 816,520" fill="var(--data-c-dark)"/>
    <rect x="750" y="520" width="88" height="24" fill="var(--data-c)"/>
    <text class="data-label" x="764" y="538">DATA C</text>
    <text class="data-figure" x="1036" y="534">40%</text>
    <text class="data-caption" x="846" y="562">plan to use social</text>
    <text class="data-caption" x="846" y="586">media even more in</text>
    <text class="data-caption" x="846" y="610">the future</text>
  </g>
</svg>
</body>
</html>
```